Bright Oak Fitness Facility Business Cards

Business Card Design that incorporates the logo and tagline

Target Market(s)

Fitness, People Who Exercise

Contact Information for Business Card

2817 Mossgrove Bend Road
Harlow Springs, Ohio 43190
Phone: 555-014-Jump (5867)
www.brightoakfitness.example
info@brightoakfitness.example

Requirements
Must have
• Logo, Address, Website, email and tagline "Train With Purpose". Colors should be red/black/grey/white

```html
<!DOCTYPE html>
<html lang="en">
<head>
<meta charset="utf-8">
<title>Bright Oak Fitness – Business Card</title>
<link rel="stylesheet" href="https://fonts.googleapis.com/css2?family=Saira:wght@600;700&display=swap">
<style>
  :root {
    --paper: #ffffff;
    --ink: #1b1817;
    --ink-soft: #2a2927;
    --red: #e52629;
    --red-bright: #d92d2a;
    --red-deep: #a81d22;
    --text-light: #d9d6d2;
  }
  * { margin: 0; padding: 0; box-sizing: border-box; }
  html, body { width: 1200px; height: 743px; overflow: hidden; background: var(--paper); }
  .card {
    position: relative;
    width: 1200px;
    height: 743px;
    background: var(--paper);
    overflow: hidden;
    font-family: "Saira", sans-serif;
  }
  .card__shapes { position: absolute; inset: 0; }

  .contact-list {
    position: absolute;
    left: 52px;
    top: 0;
    list-style: none;
  }
  .contact-item {
    position: absolute;
    left: 0;
    display: flex;
    align-items: center;
    white-space: nowrap;
  }
  .contact-item__icon {
    width: 52px;
    height: 52px;
    flex: none;
  }
  .contact-item__text {
    margin-left: 48px;
    color: var(--text-light);
    font-weight: 700;
    font-size: 22px;
    letter-spacing: 1.4px;
    line-height: 27px;
    text-transform: uppercase;
  }
  .contact-item--address { top: 374px; }
  .contact-item--phone   { top: 462px; }
  .contact-item--email   { top: 551px; }
  .contact-item--web     { top: 637px; }

  .brand {
    position: absolute;
    left: 705px;
    top: 170px;
    width: 400px;
    text-align: center;
  }
  .brand__mark {
    display: block;
    width: 66px;
    height: 66px;
    margin: 0 auto 16px;
    border-radius: 50%;
    background: var(--red);
  }
  .brand__name {
    font-weight: 700;
    font-size: 54px;
    line-height: 56px;
    color: var(--ink);
    letter-spacing: 0.5px;
    text-transform: uppercase;
  }
  .brand__rule {
    display: flex;
    align-items: center;
    gap: 10px;
    margin-top: 2px;
  }
  .brand__rule::before, .brand__rule::after {
    content: "";
    flex: 1;
    height: 3px;
    background: var(--ink);
  }
  .brand__sub {
    font-weight: 700;
    font-size: 19px;
    line-height: 22px;
    letter-spacing: 5px;
    color: var(--ink);
    text-transform: uppercase;
  }
  .brand__tagline {
    margin-top: 10px;
    font-weight: 700;
    font-size: 17px;
    line-height: 22px;
    letter-spacing: 4px;
    color: var(--ink);
    text-transform: uppercase;
  }
</style>
</head>
<body>
<main class="card">
  <svg class="card__shapes" width="1200" height="743" viewBox="0 0 1200 743" aria-hidden="true">
    <defs>
      <linearGradient id="panel-dark" x1="0" y1="1" x2="0.6" y2="0">
        <stop offset="0" stop-color="var(--ink-soft)"/>
        <stop offset="0.35" stop-color="var(--ink)"/>
      </linearGradient>
      <linearGradient id="band-red" x1="0" y1="0" x2="1" y2="0">
        <stop offset="0.55" stop-color="var(--red-bright)"/>
        <stop offset="0.85" stop-color="var(--red-deep)"/>
      </linearGradient>
    </defs>
    <polygon class="band-red" points="382,213 529,213 1058,743 910,743" fill="url(#band-red)"/>
    <polygon class="panel-dark" points="0,99 268,99 910,743 0,743" fill="url(#panel-dark)"/>
  </svg>

  <ul class="contact-list">
    <li class="contact-item contact-item--address">
      <svg class="contact-item__icon" viewBox="0 0 52 52" aria-hidden="true">
        <circle cx="26" cy="26" r="26" fill="var(--red)"/>
        <path d="M26 12c-5.5 0-9.5 4.2-9.5 9.4 0 6.6 9.5 17.6 9.5 17.6s9.5-11 9.5-17.6C35.5 16.2 31.5 12 26 12z" fill="#fff"/>
        <circle cx="26" cy="21.5" r="3.6" fill="var(--red)"/>
      </svg>
      <span class="contact-item__text">2817 Mossgrove Bend Road<br>Harlow Springs, Ohio 43190</span>
    </li>
    <li class="contact-item contact-item--phone">
      <svg class="contact-item__icon" viewBox="0 0 52 52" aria-hidden="true">
        <circle cx="26" cy="26" r="26" fill="var(--red)"/>
        <path d="M17 13.5l5 -1.5 3.5 7.5-3.2 2.5c1.6 3.6 4.2 6.4 7.6 8.3l2.7-3.1 7.4 3.6-1.4 5c-.5 1.4-1.8 2.2-3.3 2-11-1.6-19.4-10.2-20.6-21-.2-1.5.8-2.9 2.3-3.3z" fill="#fff"/>
      </svg>
      <span class="contact-item__text">555-014-Jump (5867)</span>
    </li>
    <li class="contact-item contact-item--email">
      <svg class="contact-item__icon" viewBox="0 0 52 52" aria-hidden="true">
        <circle cx="26" cy="26" r="26" fill="var(--red)"/>
        <rect x="13" y="16.5" width="26" height="19" fill="none" stroke="#fff" stroke-width="2.6"/>
        <path d="M13 17l13 10 13-10M13 35l10-9M39 35l-10-9" fill="none" stroke="#fff" stroke-width="2.4"/>
      </svg>
      <span class="contact-item__text">info@brightoakfitness.example</span>
    </li>
    <li class="contact-item contact-item--web">
      <svg class="contact-item__icon" viewBox="0 0 52 52" aria-hidden="true">
        <circle cx="26" cy="26" r="26" fill="var(--red)"/>
        <g fill="none" stroke="#fff" stroke-width="2.4">
          <circle cx="26" cy="26" r="13"/>
          <ellipse cx="26" cy="26" rx="5.5" ry="13"/>
          <path d="M13 26h26M15 19.5h22M15 32.5h22"/>
        </g>
      </svg>
      <span class="contact-item__text">www.brightoakfitness.example</span>
    </li>
  </ul>

  <header class="brand">
    <span class="brand__mark" aria-hidden="true"></span>
    <div class="brand__name">Bright Oak</div>
    <div class="brand__rule"><span class="brand__sub">Fitness</span></div>
    <p class="brand__tagline">Train With Purpose</p>
  </header>
</main>
</body>
</html>
```